National Promo Launch Needs Image Design

This image is to use for a National promotion that we will run thru "Vexo" and "Plim" campaigns. I have attached a few examples from others currently running these type of campaigns (attached docs labeled Examples and Examples2).

Should be very high-end, professional, creative, unique and modern. Should be suitable for Zenith 700 viewing.

Our technology company focuses on the Corporate Job Hiring and Recruiting industry. Our target candidate base is global and comprised of very large companies. The site relies heavily on social networking qualities.

Here is a link to the Home page:

http://mockups.orvalstudiowork.example/tarn-signal/mockups/homepage-v3/

This image should contain minimal (if any) verbiage. If you want to include our logo, it is attached. You can design it, you can source it from stock photos... as long as it relays the message appropriately. Graphic will need to be provided in PDF and PNG formats. 660px X 420px Required. Here is the message we want the graphic to symbolize:

*****TARN SIGNAL IS LOOKING FOR YOU! A $3,000 PROMOTIONAL CONTRACT IS UP FOR GRABS.
Claim your Plim Reward now for exclusive early access to our website and an opportunity to earn some cash over the next 3 months. Activating your free profile is easy and takes less than 5 minutes. At the completion of this Reward period, one lucky (and qualified) Candidate will be hand selected for participation in an upcoming promotional event for our brand. The “chosen one” will work directly with our Founder/CEO to detail strategy plan and fulfillment. Obligations will be minimal and will not interfere with existing daily responsibilities.

What if you are not selected by us? No worries… just keep your profile active. There are companies joining our site every day with similar opportunities on the horizon. Showcase your network. Realize your value.*****
Updates

I have now Guaranteed the project.  Please submit your entries as soon as possible as the deadline is approaching.

Based on the recent submissions to this project, I believe it is necessary to better explain what I am looking for here.  As stated in the initial posting:  "This image should contain minimal (if any) verbiage."

3 out of the 3 submissions have contained mostly words and very little image.

Please review the attachments/examples provided.  Minimal (if any) verbiage.  I simply included the text so you can see what this image needs to stand for.  So basically, I need an image that reflects the verbiage I posted.  However, feel free to use a few words if necessary on the image.

Thanks.

After meeting with our team, we would like see an image better reflecting Networking / Influence.  No human element.

Thanks greatly to all for your participation.

```html
<!DOCTYPE html>
<html lang="en">
<head>
<meta charset="utf-8">
<title>Tarn Signal – Promotional Contract</title>
<link rel="stylesheet" href="https://fonts.googleapis.com/css2?family=Arimo:wght@400;700&family=Nunito:wght@800&display=swap">
<style>
  :root {
    --orange: #f08a3c;
    --orange-light: #f6b07a;
    --navy: #1d3a5c;
    --grey-text: #6d6d6d;
    --status-text: #6a3512;
    --white: #ffffff;
    --room-top: #f6f6f6;
    --room-mid: #e4e4e4;
    --room-floor: #cfcfcf;
    --furniture: #bdbdbd;
  }
  * { box-sizing: border-box; margin: 0; padding: 0; }
  html, body { width: 1200px; height: 764px; overflow: hidden; background: var(--white); }
  .promo {
    position: relative;
    width: 1200px;
    height: 764px;
    overflow: hidden;
    font-family: "Arimo", Arial, sans-serif;
  }
  .office-scene {
    position: absolute;
    inset: 0;
    background:
      radial-gradient(ellipse 420px 120px at 300px 640px, rgba(150,150,150,0.35), rgba(150,150,150,0) 70%),
      linear-gradient(180deg, var(--white) 0%, var(--room-top) 40%, var(--room-mid) 68%, var(--room-floor) 100%);
  }
  .brand {
    position: absolute;
    left: 45px;
    top: 34px;
  }
  .brand-name {
    display: flex;
    align-items: center;
    gap: 12px;
    font-size: 52px;
    font-weight: 700;
    color: var(--navy);
    letter-spacing: -1px;
    line-height: 1;
  }
  .brand-mark {
    width: 14px;
    height: 14px;
    background: var(--navy);
  }
  .brand-tagline {
    margin-top: 12px;
    margin-left: 2px;
    font-size: 21px;
    color: var(--grey-text);
  }
  .feature-band {
    position: absolute;
    left: 0;
    top: 160px;
    width: 1020px;
    height: 128px;
    background: linear-gradient(90deg, var(--orange) 0%, var(--orange) 52%, var(--orange-light) 78%, rgba(246,176,122,0) 100%);
  }
  .band-icons {
    position: absolute;
    left: 0;
    top: 160px;
  }
  .offer-bubble {
    position: absolute;
    inset: 0;
    filter: drop-shadow(0 6px 14px rgba(0,0,0,0.18));
  }
  .offer-status {
    position: absolute;
    left: 600px;
    top: 290px;
    width: 405px;
    text-align: right;
    font-size: 24px;
    font-weight: 400;
    line-height: 40px;
    letter-spacing: 0.5px;
    color: var(--status-text);
  }
  .offer-status span { display: block; }
  .offer-amount {
    position: absolute;
    left: 596px;
    top: 362px;
    font-family: "Nunito", Arial, sans-serif;
    font-weight: 800;
    font-size: 138px;
    line-height: 1;
    letter-spacing: 4px;
    color: var(--white);
  }
  .offer-details {
    position: absolute;
    left: 575px;
    top: 522px;
    width: 460px;
    text-align: center;
    font-size: 21px;
    line-height: 35px;
    color: var(--white);
  }
</style>
</head>
<body>
<main class="promo">
  <div class="office-scene" role="img" aria-label="Bright modern office interior with a desk, chair, lamp and sofa"></div>

  <header class="brand">
    <div class="brand-name"><span class="brand-mark"></span>Tarn Signal</div>
    <p class="brand-tagline">The Source for Networking Superstars</p>
  </header>

  <div class="feature-band"></div>

  <svg class="band-icons" width="1000" height="128" viewBox="0 0 1000 128" aria-label="Candidate profile, global search and professional network icons" role="img">
    <line x1="0" y1="78" x2="880" y2="78" stroke="#ffffff" stroke-width="2" stroke-dasharray="2 4"/>
    <g class="icon-candidate" fill="#ffffff" stroke="#ffffff">
      <circle cx="96" cy="28" r="13" stroke="none"/>
      <path d="M78 46 h36 v36 h-6 v36 h-9 v-30 h-6 v30 h-9 v-36 h-6 z" stroke="none"/>
      <circle cx="130" cy="98" r="22" fill="#f08a3c" stroke-width="4"/>
      <circle cx="130" cy="92" r="6" stroke="none"/>
      <path d="M118 110 q12 -16 24 0 z" stroke="none"/>
    </g>
    <g class="icon-search" fill="none" stroke="#ffffff" stroke-width="4" stroke-linecap="round">
      <circle cx="318" cy="58" r="34"/>
      <ellipse cx="318" cy="58" rx="14" ry="34" stroke-width="2.5"/>
      <line x1="284" y1="58" x2="352" y2="58" stroke-width="2.5"/>
      <line x1="290" y1="42" x2="346" y2="42" stroke-width="2.5"/>
      <line x1="290" y1="74" x2="346" y2="74" stroke-width="2.5"/>
      <circle cx="348" cy="78" r="20" fill="#f08a3c" stroke-width="5"/>
      <line x1="362" y1="93" x2="390" y2="120" stroke-width="9"/>
    </g>
    <g class="icon-network" fill="#ffffff">
      <circle cx="565" cy="40" r="14"/>
      <path d="M540 100 q0 -38 25 -38 q25 0 25 38 z"/>
      <circle cx="522" cy="58" r="14"/>
      <path d="M497 118 q0 -38 25 -38 q25 0 25 38 z" stroke="#f08a3c" stroke-width="3"/>
    </g>
  </svg>

  <svg class="offer-bubble" width="1200" height="764" viewBox="0 0 1200 764" aria-hidden="true">
    <defs>
      <radialGradient id="bubbleFill" cx="0.45" cy="0.5" r="0.6">
        <stop offset="0" stop-color="#f39a52"/>
        <stop offset="1" stop-color="#ee8030"/>
      </radialGradient>
    </defs>
    <path d="M1131 457 A285 250 0 1 1 1068 339 Q1140 272 1195 168 Q1148 300 1131 457 Z"
          fill="url(#bubbleFill)" stroke="#ffffff" stroke-width="8" stroke-linejoin="round"/>
  </svg>

  <h2 class="offer-status"><span>AVAILABLE NOW</span><span>PROMOTIONAL CONTRACT</span></h2>
  <p class="offer-amount">$3,000</p>
  <p class="offer-details">Claim your Plim Reward now for exclusive<br>early access to our website and an<br>opportunity to earn some cash over<br>the next 3 months.</p>
</main>
</body>
</html>
```